Golden Lark Hour Gin label

I’m looking for a gin label that as the title says it should be a bright and fun filled label for . The gin will have four seasons so each season will have a different label starting with a summer gin. It should be fright and cooler full happy and fun The name of the Gin is Golden Lark Hour Gin it should be bright and jump off the shelf.

Target Market(s)

Gin buyers

Font styles to use
Decorative
Script

Colors

Designer to choose colors to be used in the design.

Requirements
Must have
• Bright colours interesting eye catching

```html
<!DOCTYPE html>
<html lang="en">
<head>
<meta charset="utf-8">
<title>Golden Lark Hour Gin – Seasonal Labels</title>
<link rel="stylesheet" href="https://fonts.googleapis.com/css2?family=Cinzel:wght@400;600;700&family=Dancing+Script:wght@600;700&family=Arimo:wght@400&display=swap">
<style>
  :root {
    --ink: #0f3d86;
    --stage: #eceded;
    --stage-light: #f7f7f7;
    --title-grey: #6b6b6b;
    --frame-silver: #c9ccd1;
    --paper: #ffffff;
  }
  html, body {
    margin: 0;
    padding: 0;
    width: 1200px;
    height: 1200px;
    overflow: hidden;
  }
  body {
    background: radial-gradient(ellipse at center, var(--stage-light) 0%, var(--stage) 80%);
    font-family: "Cinzel", serif;
  }
  .label-range {
    position: absolute;
    left: 50px;
    top: 330px;
    display: flex;
    gap: 40px;
  }
  .season {
    width: 340px;
    display: flex;
    flex-direction: column;
    align-items: center;
  }
  .season-title {
    font-family: "Arimo", sans-serif;
    font-size: 22px;
    letter-spacing: 0.5px;
    color: var(--title-grey);
    margin: 0 0 34px;
    font-weight: 400;
  }
  .label { display: block; width: 340px; height: 453px; }
  .label--summer { --sun: #ffd733; --ribbon: #4fc5e0; --dot: #4fc5e0; --base: var(--paper); }
  .label--autumn { --sun: #f5a79b; --ribbon: #f8c9ae; --dot: #0b4a78; --base: var(--paper); }
  .label--winter { --sun: #9ed9e4; --ribbon: #0b4a78; --dot: #0b4a78; --base: #f7f6f4; }
  .label-base { fill: var(--base); }
  .sun { fill: var(--sun); }
  .sun-ring { fill: none; stroke: var(--sun); stroke-width: 6; opacity: 0.55; }
  .ribbon { fill: var(--ribbon); }
  .ribbon-thin { fill: var(--dot); }
  .dot { fill: var(--dot); }
  .frame { fill: none; stroke: var(--frame-silver); stroke-width: 2; }
  .rule { stroke: var(--ink); stroke-width: 2; }
  .label text { fill: var(--ink); font-family: "Cinzel", serif; text-anchor: middle; }
  .maker { font-size: 15px; font-weight: 600; letter-spacing: 0.3px; }
  .est { font-size: 15px; }
  .name-top { font-size: 44px; font-weight: 700; letter-spacing: 1px; }
  .label text.name-script { font-family: "Dancing Script", cursive; font-size: 44px; font-weight: 700; }
  .name-gin { font-size: 88px; font-weight: 700; }
  .volume { font-size: 14px; font-weight: 600; }
</style>
</head>
<body>

<svg width="0" height="0" style="position:absolute" aria-hidden="true">
  <defs>
    <clipPath id="label-shape">
      <path d="M28 0 H392 Q420 0 420 28 V540 Q420 560 400 560 H20 Q0 560 0 540 V28 Q0 0 28 0 Z"/>
    </clipPath>
    <g id="label-art">
      <rect class="label-base" width="420" height="560"/>
      <circle class="sun-ring" cx="330" cy="150" r="178"/>
      <circle class="sun" cx="330" cy="150" r="150"/>
      <circle class="dot" cx="58" cy="78" r="34"/>
      <path class="ribbon" d="M0 450 C70 420 140 480 210 450 S350 420 420 450 L420 485 C350 455 280 515 210 485 S70 455 0 485 Z"/>
      <path class="ribbon-thin" d="M0 496 C70 466 140 526 210 496 S350 466 420 496 L420 506 C350 476 280 536 210 506 S70 476 0 506 Z"/>
      <rect class="label-base" x="76" y="139" width="263" height="263" opacity="0"/>
      <rect class="frame" x="70" y="133" width="275" height="275"/>
      <rect class="frame" x="76" y="139" width="263" height="263"/>
    </g>
  </defs>
</svg>

<main class="label-range">
  <section class="season">
    <h2 class="season-title">SUMMER GIN</h2>
    <svg class="label label--summer" viewBox="0 0 420 560" role="img" aria-label="Golden Lark Hour Gin summer label">
      <g clip-path="url(#label-shape)"><use href="#label-art"/></g>
      <text class="maker" x="210" y="62">LARKSPUR STILL CO</text>
      <text class="est" x="210" y="166">EST. 1984</text>
      <line class="rule" x1="165" y1="178" x2="255" y2="178"/>
      <text class="name-top" x="210" y="230">GOLDEN</text>
      <text class="name-script" x="210" y="276">Lark Hour</text>
      <text class="name-gin" x="210" y="360">GIN</text>
      <line class="rule" x1="165" y1="378" x2="255" y2="378"/>
      <text class="volume" x="210" y="538">750 ML 42% ALC. VOL.</text>
    </svg>
  </section>

  <section class="season">
    <h2 class="season-title">AUTUMN GIN</h2>
    <svg class="label label--autumn" viewBox="0 0 420 560" role="img" aria-label="Golden Lark Hour Gin autumn label">
      <g clip-path="url(#label-shape)"><use href="#label-art"/></g>
      <text class="maker" x="210" y="62">LARKSPUR STILL CO</text>
      <text class="est" x="210" y="166">EST. 1984</text>
      <line class="rule" x1="165" y1="178" x2="255" y2="178"/>
      <text class="name-top" x="210" y="230">GOLDEN</text>
      <text class="name-script" x="210" y="276">Lark Hour</text>
      <text class="name-gin" x="210" y="360">GIN</text>
      <line class="rule" x1="165" y1="378" x2="255" y2="378"/>
      <text class="volume" x="210" y="538">750 ML 42% ALC. VOL.</text>
    </svg>
  </section>

  <section class="season">
    <h2 class="season-title">WINTER GIN</h2>
    <svg class="label label--winter" viewBox="0 0 420 560" role="img" aria-label="Golden Lark Hour Gin winter label">
      <g clip-path="url(#label-shape)"><use href="#label-art"/></g>
      <text class="est" x="210" y="166">EST. 1984</text>
      <line class="rule" x1="165" y1="178" x2="255" y2="178"/>
      <text class="name-top" x="210" y="226">GOLDEN</text>
      <text class="name-script" x="210" y="270">Lark Hour</text>
      <text class="name-gin" x="210" y="350">GIN</text>
      <line class="rule" x1="165" y1="364" x2="255" y2="364"/>
      <text class="maker" x="210" y="388">LARKSPUR STILL CO</text>
      <text class="volume" x="210" y="538">750 ML 42% ALC. VOL.</text>
    </svg>
  </section>
</main>

</body>
</html>
```